Need modern simple design for magazine ad, apartment and condo roofer.

I need a half page magazine ad for a local roofer to publish in an industry magazine. Apartment associations industry. All types of roofs. Shingle and Flat
Need the design to be creative and modern, clean and simple. I do not want a busy design. One that stands out and makes a point quickly.
Logo must be prominent.
DO NOT USE PHOTOS FROM MY WEBSITE PLEASE. Looking for something new.
I work on entire complexes not houses.

Need to make sure our phone number and email address are listed at the bottom. Here is my website www.vorbelan.com
Want to stay away from standard clip arts of tools, homes, apartment buildings.
Half Horizontal 7.25 x 4.75
Ads should be in PDF and JPG format.

Target Market(s)

Apartment or Condo owners looking for large scale roofing projects

Industry/Entity Type

Roofing

Requirements
Must have
• Prominent Logo
Simple Clean Design
Create graphics
Not Busy
Should not have
• Clip Art
No Photos from my website

```html
<!DOCTYPE html>
<html lang="en">
<head>
<meta charset="utf-8">
<title>Vorbelan Roofing – Half Page Ad</title>
<link rel="stylesheet" href="https://fonts.googleapis.com/css2?family=Oswald:wght@500;600&family=Pathway+Gothic+One&family=Roboto+Condensed:wght@400;900&display=swap">
<style>
  :root{
    --sky-top:#3f74c4;
    --sky-mid:#7ea3d6;
    --roof-light:#a9b2bf;
    --roof-dark:#5e6775;
    --band-blue:#2456a4;
    --panel-blue:rgba(24,74,170,0.82);
    --logo-black:#000000;
    --silver:#c9ccd1;
    --white:#ffffff;
    --footer-blue:#2a5ca8;
  }
  *{margin:0;padding:0;box-sizing:border-box}
  html,body{width:1200px;height:783px;overflow:hidden;background:var(--white)}
  .ad{position:relative;width:1200px;height:783px;overflow:hidden;font-family:"Pathway Gothic One",sans-serif;color:var(--white)}

  .hero-image{position:absolute;left:0;top:0;width:1200px;height:699px;
    background:
      linear-gradient(160deg,transparent 45%,rgba(94,103,117,0.9) 46%,var(--roof-light) 70%,var(--roof-dark) 100%),
      linear-gradient(180deg,var(--sky-top) 0%,var(--sky-mid) 45%,#c9d6e6 60%);
  }
  .top-band{position:absolute;left:373px;top:0;width:827px;height:25px;background:var(--band-blue)}

  .side-panel{position:absolute;left:33px;top:0;width:340px;height:699px;background:var(--panel-blue)}
  .logo-block{position:absolute;left:33px;top:0;width:340px;height:134px;background:var(--logo-black);
    display:flex;align-items:center;justify-content:center;gap:12px}
  .logo-square{width:34px;height:34px;background:var(--silver)}
  .logo-name{font-family:"Oswald",sans-serif;font-weight:600;font-size:38px;line-height:1;color:var(--silver);letter-spacing:.5px}

  .arrow{position:absolute}
  .arrow-side{left:185px;top:124px}
  .arrow-top{left:743px;top:15px}

  .intro{position:absolute;left:48px;top:228px;width:310px;font-size:25.5px;line-height:27.6px}
  .intro .line{display:block;white-space:nowrap;text-align:justify;text-align-last:justify}
  .intro .line.last{text-align-last:left}
  .intro strong{font-weight:400;-webkit-text-stroke:.6px var(--white);letter-spacing:.3px}
  .promise{position:absolute;left:48px;top:528px;width:320px;font-size:30px;line-height:35px;white-space:nowrap}

  .headline{position:absolute;right:35px;top:56px;text-align:right;font-family:"Oswald",sans-serif;font-weight:500;
    font-size:54px;line-height:52px;text-transform:uppercase;text-shadow:2px 3px 4px rgba(0,0,0,.35);
    letter-spacing:-.5px;white-space:nowrap;transform:scaleX(.84);transform-origin:right top}

  .service-lead{position:absolute;left:686px;top:355px;font-family:"Roboto Condensed",sans-serif;font-weight:900;font-size:70px;line-height:1;white-space:nowrap;letter-spacing:-2px}
  .service-word{position:absolute;right:37px;top:378px;font-family:"Roboto Condensed",sans-serif;font-weight:900;font-size:206px;line-height:1;letter-spacing:-9px;white-space:nowrap}
  .service-note{position:absolute;right:35px;top:596px;font-size:74px;line-height:1;white-space:nowrap}

  .footer-rule{position:absolute;left:0;top:699px;width:1200px;height:5px;background:var(--white)}
  .footer{position:absolute;left:0;top:704px;width:1200px;height:79px;background:var(--footer-blue);font-size:26px}
  .contact{position:absolute;top:0;height:79px;display:flex;align-items:center;gap:12px;white-space:nowrap}
  .contact-address{left:114px}
  .contact-phone{left:663px}
  .contact-email{left:889px}
  .at{font-family:"Roboto Condensed",sans-serif;font-size:24px;font-weight:900}
</style>
</head>
<body>
<div class="ad">
  <div class="hero-image" role="img" aria-label="Photograph of a grey shingled pitched roof with brick chimney and gable vents against a blue sky with white clouds"></div>
  <div class="top-band"></div>

  <div class="side-panel"></div>
  <div class="logo-block">
    <span class="logo-square"></span>
    <span class="logo-name">Vorbelan Roofing</span>
  </div>

  <svg class="arrow arrow-side" width="36" height="102" viewBox="0 0 36 102" aria-hidden="true">
    <path d="M9 2 Q9 0 14 0 H27 V68 H36 L18 102 L0 68 H9 Z" fill="#fff"/>
  </svg>
  <svg class="arrow arrow-top" width="36" height="45" viewBox="0 0 36 45" aria-hidden="true">
    <path d="M9 2 Q9 0 14 0 H27 V24 H36 L18 45 L0 24 H9 Z" fill="#fff"/>
  </svg>

  <p class="intro">
    <span class="line"><strong>VORBELAN ROOFING</strong>, has been</span>
    <span class="line">improving and adding value to</span>
    <span class="line">multifamily apartment communities</span>
    <span class="line">and student housing developments for</span>
    <span class="line">over 30 years now. Although we have</span>
    <span class="line">done work in many other states, most</span>
    <span class="line">of our projects are in the great state of</span>
    <span class="line">Texas. From the simple to the lavish,</span>
    <span class="line">we’ve experienced it all and we can</span>
    <span class="line last">help you every step of the way.</span>
  </p>
  <p class="promise">No job is too small or too big<br>for our knowledgeable crews.</p>

  <h1 class="headline">We do work on entire<br>complexes not just houses</h1>

  <span class="service-word">Roofing</span>
  <span class="service-lead">We do</span>
  <span class="service-note">(all types)</span>

  <div class="footer-rule"></div>
  <footer class="footer">
    <span class="contact contact-address">
      <svg width="20" height="26" viewBox="0 0 22 28" aria-hidden="true"><path d="M11 0C5 0 0 5 0 11c0 8 11 17 11 17s11-9 11-17C22 5 17 0 11 0zm0 16a5 5 0 1 1 0-10 5 5 0 0 1 0 10z" fill="#fff"/></svg>
      412 Meridian Avenue, Suite 210, Grapevine, TX 76051
    </span>
    <span class="contact contact-phone">
      <svg width="28" height="28" viewBox="0 0 24 24" aria-hidden="true"><path d="M6.6 10.8a15 15 0 0 0 6.6 6.6l2.2-2.2a1 1 0 0 1 1-.25 11.4 11.4 0 0 0 3.6.57 1 1 0 0 1 1 1V20a1 1 0 0 1-1 1A17 17 0 0 1 3 4a1 1 0 0 1 1-1h3.5a1 1 0 0 1 1 1c0 1.250.2 2.450.57 3.570a1 1 0 0 1-.25 1z" fill="#fff"/></svg>
      817.555.0148
    </span>
    <span class="contact contact-email">
      <span class="at">@</span>
      info@vorbelan.com
    </span>
  </footer>
</div>
</body>
</html>
```